**Business Card**Designs Project** LornaTrade,LLC

Im looking for a simple and elegant Business Card that has a professional Corporate look and feel. Im considering a Metal business card as well as 2 color layout, Embossed, 1 color two tone layout(File#6 like).

The card should NOT be too busy but subtle. Clean look providing Key Details.

please see uploaded files for actual logo and inspirational design i like.

See Uploaded File # 3 for Professional Logos Style

Target Market(s)

investors

Industry/Entity Type

Business

Contact Information for Business Card

Side 1 information
Lorna Trade,LLC - Description Text below main logo = (Funding - Sales) or (Commercial - Residential) or (Property - Funding )
www.lornatrade-demo.com

Side 2 Information =
Dov Pelkin | Managing Broker
P 555-014-7781 | F 555-016-2490
E info@lornatrade-demo.com
membership logos - see file #3 for stye and file #4 for inspiration

Side 2 = 10pt Font
BRE: 07281944
NMLS: 6620573

Colors
3277b5
5c5c5c
333333
959595
85acd3
1b1b1b
ffffff

Requirements
Must have
• Lorna Trade, LLC **G Logo** - See Uploaded File #5 ,
• Contact Information - See Business Card Details Above
• Web address = www.lornatrade-demo.com
• Membership logos - See Uploaded File #4 & 9
Nice to have
• 1 Color two tones, grey, White, Charcoal Grey, Dark Turquois, Dark blue, Slate blue,
• GOOD COMBINATIONS: White and Grey, white and Charcoal grey with a splash of blue, Charcoal grey card with White, etc..
• PLEASE TRY DARK BLUE DESIGNS
• Embossed, card designs
• Metal Business card design
Should not have
• I DONT LIKE ALOTE OF WAVE DESIGNS

```html
<!DOCTYPE html>
<html lang="en">
<head>
<meta charset="utf-8">
<title>Lorna Trade LLC – Business Card</title>
<link rel="stylesheet" href="https://fonts.googleapis.com/css2?family=Exo+2:wght@400;500;700&display=swap">
<style>
  :root {
    --blue: #2a8bbf;
    --grey: #5c5c5c;
    --charcoal: #333333;
    --light-grey: #959595;
    --white: #ffffff;
    --page: #ecebe8;
  }
  * { margin: 0; padding: 0; box-sizing: border-box; }
  html, body { width: 1200px; height: 1018px; overflow: hidden; }
  body {
    background: var(--page);
    font-family: "Exo 2", "Helvetica Neue", Arial, sans-serif;
    position: relative;
  }
  .card {
    position: absolute;
    left: 220px;
    width: 760px;
    height: 434px;
    overflow: hidden;
    box-shadow: 0 6px 18px rgba(0,0,0,0.18);
  }
  .card--contact { top: 45px; background: var(--white); }
  .card--brand { top: 539px; }

  /* Contact side: brand zone */
  .brand {
    position: absolute; left: 0; top: 0; width: 100%; height: 200px;
    display: flex; align-items: center; padding-left: 70px;
  }
  .brand__mark {
    width: 70px; height: 70px; border-radius: 50%;
    background: var(--blue); flex: none;
  }
  .brand__divider {
    width: 2px; height: 92px; background: var(--light-grey);
    margin: 0 22px 0 26px;
  }
  .brand__name {
    font-size: 40px; font-weight: 500; color: var(--grey);
    letter-spacing: 1px; line-height: 1;
  }
  .brand__rule { width: 250px; height: 2px; background: var(--grey); margin: 10px 0 8px; }
  .brand__tagline {
    font-size: 15px; color: var(--grey); letter-spacing: 2.5px; text-transform: uppercase;
  }

  /* Contact side: contact band */
  .contact-band {
    position: absolute; left: 0; top: 200px; width: 100%; height: 100px;
    background: var(--blue); color: var(--white);
    padding: 22px 0 0 60px; font-size: 16px; letter-spacing: 1px;
    display: grid; grid-template-columns: 230px auto; row-gap: 14px;
  }
  .contact-item { display: flex; align-items: center; gap: 10px; white-space: nowrap; }
  .contact-item svg { width: 16px; height: 16px; flex: none; }
  .contact-item__label { font-weight: 700; }

  /* Contact side: identity band */
  .identity-band {
    position: absolute; left: 0; top: 300px; width: 100%; height: 134px;
    background: var(--grey); color: var(--white);
    display: flex; justify-content: space-between; align-items: center;
    padding: 0 50px 0 60px;
  }
  .person__name { font-size: 30px; font-weight: 700; letter-spacing: 1px; text-transform: uppercase; }
  .person__role { font-size: 16px; letter-spacing: 2px; text-transform: uppercase; margin-top: 4px; }
  .licences { display: flex; align-items: center; gap: 22px; }
  .licences__numbers { font-size: 16px; letter-spacing: 1px; text-align: right; line-height: 1.6; }
  .memberships { display: flex; gap: 10px; }
  .membership-badge {
    width: 40px; height: 40px; border: 2px solid var(--white);
    border-radius: 50%; opacity: 0.85;
  }
  .membership-badge--square { border-radius: 0; }

  /* Brand side */
  .back-pattern { position: absolute; inset: 0; display: block; width: 100%; height: 100%; }
  .brand-side {
    position: absolute; inset: 0;
    display: flex; flex-direction: column; align-items: center; justify-content: center;
    color: var(--white); text-align: center;
  }
  .brand-side__mark { width: 56px; height: 56px; border-radius: 50%; background: var(--white); margin-bottom: 18px; }
  .brand-side__name { font-size: 40px; font-weight: 500; letter-spacing: 1px; line-height: 1; }
  .brand-side__rule { width: 250px; height: 2px; background: var(--white); margin: 12px 0 10px; }
  .brand-side__tagline { font-size: 15px; letter-spacing: 2.5px; text-transform: uppercase; }
  .brand-side__web { font-size: 16px; letter-spacing: 1px; margin-top: 26px; }
</style>
</head>
<body>

  <section class="card card--contact" aria-label="Business card contact side">
    <div class="brand">
      <div class="brand__mark" aria-hidden="true"></div>
      <div class="brand__divider" aria-hidden="true"></div>
      <div class="brand__text">
        <div class="brand__name">LORNA TRADE, LLC</div>
        <div class="brand__rule" aria-hidden="true"></div>
        <div class="brand__tagline">Commercial &amp; Residential</div>
      </div>
    </div>

    <div class="contact-band">
      <div class="contact-item">
        <svg viewBox="0 0 16 16" aria-hidden="true"><path fill="#fff" d="M3.5 1.5l2.5 3-1.5 1.5c.8 1.8 2.2 3.2 4 4l1.5-1.5 3 2.5-1.5 2.5C6.5 13.5 2.5 9.5 1 4z"/></svg>
        <span><span class="contact-item__label">P</span> 555-014-7781</span>
      </div>
      <div class="contact-item">
        <svg viewBox="0 0 16 16" aria-hidden="true"><rect x="1" y="3" width="14" height="10" fill="#fff"/><path d="M1 3l7 5 7-5" fill="none" stroke="#2a8bbf" stroke-width="1.3"/></svg>
        <span><span class="contact-item__label">E</span> info@lornatrade-demo.com</span>
      </div>
      <div class="contact-item">
        <svg viewBox="0 0 16 16" aria-hidden="true"><rect x="3" y="1" width="10" height="5" fill="none" stroke="#fff" stroke-width="1.3"/><rect x="1" y="6" width="14" height="7" fill="#fff"/><rect x="4" y="10" width="8" height="5" fill="#2a8bbf" stroke="#fff" stroke-width="1"/></svg>
        <span><span class="contact-item__label">F</span> 555-016-2490</span>
      </div>
    </div>

    <div class="identity-band">
      <div class="person">
        <div class="person__name">Dov Pelkin</div>
        <div class="person__role">Managing Broker</div>
      </div>
      <div class="licences">
        <div class="licences__numbers">BRE: 07281944<br>NMLS: 6620573</div>
        <div class="memberships" role="img" aria-label="Membership badges">
          <div class="membership-badge"></div>
          <div class="membership-badge membership-badge--square"></div>
        </div>
      </div>
    </div>
  </section>

  <section class="card card--brand" aria-label="Business card brand side">
    <svg class="back-pattern" viewBox="0 0 760 434" preserveAspectRatio="none" aria-hidden="true">
      <rect width="760" height="434" fill="#2a8bbf"/>
      <polygon points="170,0 300,0 70,434 -60,434" fill="#5c5c5c"/>
      <polygon points="520,0 610,0 380,434 290,434" fill="#5c5c5c"/>
    </svg>
    <div class="brand-side">
      <div class="brand-side__mark" aria-hidden="true"></div>
      <div class="brand-side__name">LORNA TRADE, LLC</div>
      <div class="brand-side__rule" aria-hidden="true"></div>
      <div class="brand-side__tagline">Commercial &amp; Residential</div>
      <div class="brand-side__web">www.lornatrade-demo.com</div>
    </div>
  </section>

</body>
</html>
```